website design for a new age Real Estate Security Business

We are launching a business in real estate which no body else is doing. We are going to use technology in terms of software and hardware to provide our services.

We are going to use Big Data, IOT etc.. for our services.

NOTE: We don't want to see Shiel or buildings etc.. that directly suggests Real estate or security on this design

Target Market(s)

India

Industry/Entity Type

Real Estate

Number of Pages Required

4 page

Font styles to use
Sans Serif
Other font styles liked:
• Use Google Fonts

Requirements
Must have
• Home Page should be trendy and colourful should give user confidence to subscribe to our service.
Nice to have
• Use Google fonts.
Should not have
• Design shouldnt have Shield or Buildings that directly suggests real estate or security.

```html
<!DOCTYPE html>
<html lang="en">
<head>
<meta charset="utf-8">
<title>Terranova Watch</title>
<link href="https://fonts.googleapis.com/css2?family=Roboto:ital,wght@0,400;0,500;0,700;1,400&family=Open+Sans:ital,wght@0,400;0,600;1,400&display=swap" rel="stylesheet">
<style>
:root{
  --ink:#1d1d1d;
  --text:#555;
  --muted:#777;
  --accent:#1fb3ea;
  --orange:#f7773b;
  --line:#cfcfcf;
  --hero-dark:#07131c;
  --hero-teal:#1f6d6a;
  --white:#fff;
}
*{box-sizing:border-box;margin:0;padding:0}
html,body{width:719px;height:1200px;overflow:hidden;background:var(--white)}
body{position:relative;font-family:"Open Sans",Arial,sans-serif;color:var(--text)}

/* hero */
.hero{position:absolute;left:0;top:0;width:719px;height:350px;overflow:hidden}
.hero-bg{position:absolute;inset:0;background:radial-gradient(ellipse at 70% 75%,#2a8d85 0%,var(--hero-teal) 22%,#0d2e36 55%,var(--hero-dark) 85%)}
.hero-curve{position:absolute;left:0;top:285px}
.nav{position:absolute;top:26px;left:58px;right:58px;display:flex;align-items:center}
.brand{font-family:"Roboto",sans-serif;font-weight:700;font-size:15.5px;color:var(--white);letter-spacing:.2px}
.menu{margin-left:auto;display:flex;list-style:none;align-items:center}
.menu li{font-family:"Roboto",sans-serif;font-weight:500;font-size:9.5px;color:var(--white);margin-left:30px}
.menu li.active{color:var(--accent)}
.tagline{position:absolute;left:60px;top:219px;font-family:"Open Sans",sans-serif;font-style:italic;font-size:13px;color:var(--white)}
.btn{display:inline-block;background:var(--orange);color:var(--white);font-family:"Roboto",sans-serif;font-weight:500;border-radius:14px;text-align:center}
.hero .btn{position:absolute;left:61px;top:252px;width:92px;height:26px;line-height:26px;font-size:10px}
.dots{position:absolute;left:338px;top:281px;display:flex;gap:3px}
.dots span{width:8px;height:8px;border-radius:50%;border:1.2px solid var(--white)}
.dots span.on{background:var(--white)}

/* welcome */
.section-title{position:absolute;left:0;width:719px;text-align:center;font-family:"Roboto",sans-serif;font-weight:700;color:var(--ink);font-size:17.5px}
.intro{position:absolute;left:100px;width:519px;top:424px;text-align:center;font-size:8.3px;line-height:17.5px;color:var(--text)}
.card{position:absolute;top:493px;width:245px;height:131px;border:1px solid var(--line)}
.card h3{position:absolute;top:18px;font-family:"Roboto",sans-serif;font-weight:500;font-size:13px;color:var(--ink)}
.card p{position:absolute;top:42px;width:160px;font-size:8.2px;line-height:16px;color:var(--text)}
.card .more{position:absolute;top:101px;font-family:"Roboto",sans-serif;font-weight:500;font-size:8.5px;color:var(--orange)}
.card-left h3,.card-left p,.card-left .more{right:72px;text-align:right}
.card-right h3,.card-right p,.card-right .more{left:70px}
.badge{position:absolute;top:512px;width:94px;height:94px;border-radius:50%;border:1px solid var(--line);background:var(--white);display:flex;align-items:center;justify-content:center}

/* plan */
.plan{position:absolute;left:0;top:673px;width:719px;height:184px}
.plan-bg{position:absolute;inset:0;background:linear-gradient(100deg,#2b2a2c 0%,#5a4a3d 35%,#7a6048 55%,#4d3f33 80%,#2f2a26 100%)}
.plan-shade{position:absolute;inset:0;background:rgba(0,0,0,.25)}
.plan .section-title{top:34px;color:var(--white)}
.plan p{position:absolute;left:148px;width:423px;top:68px;text-align:center;font-size:8.2px;line-height:15px;color:var(--white)}
.plan .btn{position:absolute;left:310px;top:125px;width:99px;height:24px;line-height:24px;font-size:8.8px}

/* contact */
.col-title{position:absolute;font-family:"Roboto",sans-serif;font-weight:400;font-size:12.5px;color:#333;letter-spacing:.2px}
.field{position:absolute;border:1px solid var(--line);font-size:7px;color:var(--muted);padding:6px 9px}
.submit{position:absolute;left:373px;top:1106px;width:64px;height:24px;line-height:24px;font-size:9px;font-weight:700}
.info-icon{position:absolute;left:478px;width:21px;height:21px;border-radius:50%;border:1px solid var(--line);display:flex;align-items:center;justify-content:center}
.info-text{position:absolute;left:526px;font-size:7px;line-height:14.5px;color:#444}
.newsletter{position:absolute;left:478px;top:1105px;width:181px;height:24px;display:flex}
.newsletter .email{flex:1;border:1px solid var(--line);font-size:7.5px;color:var(--muted);padding:6px 10px}
.newsletter .go{width:51px;background:var(--orange);color:var(--white);font-family:"Roboto",sans-serif;font-weight:500;font-size:8px;text-align:center;line-height:24px}

.footer-rule{position:absolute;left:58px;right:60px;top:1148px;border-top:1px solid var(--line)}
.copyright{position:absolute;left:58px;top:1168px;font-size:7px;color:#555}
.social{position:absolute;top:1162px;display:flex;gap:6px;left:562px}
.social span{width:20px;height:20px;border-radius:50%}
</style>
</head>
<body>

<header class="hero">
  <div class="hero-bg" role="img" aria-label="Dark abstract network of glowing teal data points with a data, analysis and action flow graphic"></div>
  <svg class="hero-curve" width="719" height="65" viewBox="0 0 719 65">
    <path d="M0 8 Q360 95 719 8 L719 65 L0 65 Z" fill="#fff"/>
    <path d="M0 8 Q360 95 719 8" fill="none" stroke="#1fb3ea" stroke-width="6"/>
  </svg>

  <nav class="nav">
    <div class="brand">TERRANOVA WATCH</div>
    <ul class="menu">
      <li class="active">HOME</li>
      <li>SERVICES</li>
      <li>CONTACT US</li>
      <li>PRICING</li>
      <li>
        <svg width="9" height="9" viewBox="0 0 10 10"><circle cx="4" cy="4" r="3" fill="none" stroke="#fff" stroke-width="1.6"/><path d="M6.3 6.3 9 9" stroke="#fff" stroke-width="1.8"/></svg>
      </li>
    </ul>
  </nav>

  <p class="tagline">To keep your property Safe</p>
  <a class="btn">LEARN MORE</a>
  <div class="dots"><span class="on"></span><span></span><span></span><span></span></div>
</header>

<section class="welcome">
  <h2 class="section-title" style="top:388px">WELCOME TO TERRANOVA WATCH</h2>
  <p class="intro">Nemo enim ipsam voluptatem quia voluptas sit aspernatur aut odit aut fugit, sed quia consequuntur magni dolores eos qui ratione voluptatem sequi nesciue porro quisquam est, qui dolorem ipsum quia dolor sit amet, consectetur, adipisci velit</p>

  <article class="card card-left" style="left:59px">
    <h3>DOC SECURE</h3>
    <p>Neque porro quisquam est, qui dolorem ipsum quia dolor sit amet, consectetu ad ipisci vel d quia non numqua.</p>
    <span class="more">READ MORE</span>
  </article>
  <div class="badge" style="left:254px">
    <svg width="36" height="42" viewBox="0 0 36 42">
      <path d="M2 2 H24 L34 12 V40 H2 Z" fill="#1fb3ea"/>
      <path d="M24 2 V12 H34" fill="#fff" opacity=".6"/>
      <rect x="9" y="20" width="18" height="2.5" fill="#fff"/>
      <rect x="9" y="26" width="18" height="2.5" fill="#fff"/>
      <rect x="9" y="32" width="18" height="2.5" fill="#fff"/>
    </svg>
  </div>

  <article class="card card-right" style="left:415px">
    <h3>LAND SECURE</h3>
    <p>Neque porro quisquam est, qui dolorem ipsum quia dolor sit amet, consectetu ad ipisci vel d quia non numqua.</p>
    <span class="more">READ MORE</span>
  </article>
  <div class="badge" style="left:370px">
    <svg width="32" height="42" viewBox="0 0 32 42">
      <path d="M16 40 C6 26 3 20 3 14 A13 13 0 0 1 29 14 C29 20 26 26 16 40 Z" fill="#1fb3ea"/>
      <circle cx="16" cy="14" r="5" fill="#fff"/>
    </svg>
  </div>
</section>

<section class="plan">
  <div class="plan-bg" role="img" aria-label="Photo of hands typing on a laptop on a wooden desk"></div>
  <div class="plan-shade"></div>
  <h2 class="section-title">CHOOSE YOUR PLAN</h2>
  <p>Neque porro quisquam est, qui dolorem ipsum quia dolor sit amet, consectetur, adipisci velit, sed quia non numquam eius modi tempora incidunt ut labore et dolore magnam aliquam quaerat voluptatem. Ut enim ad minima veniam, quis nostrum exercitationem ullam corporis susci</p>
  <a class="btn">VIEW OUR PRICING</a>
</section>

<section class="contact">
  <h2 class="section-title" style="top:904px">CONTACT US</h2>

  <h3 class="col-title" style="left:58px;top:953px">Contact form</h3>
  <div class="field" style="left:59px;top:993px;width:187px;height:20px">Name :</div>
  <div class="field" style="left:251px;top:993px;width:186px;height:20px">Phone no :</div>
  <div class="field" style="left:59px;top:1020px;width:378px;height:20px">Email :</div>
  <div class="field" style="left:59px;top:1047px;width:378px;height:50px;padding-top:9px">Message :</div>
  <a class="btn submit">SUBMIT</a>

  <h3 class="col-title" style="left:478px;top:954px">Contact Information</h3>
  <div class="info-icon" style="top:983px">
    <svg width="8" height="10" viewBox="0 0 8 10"><path d="M4 10 C1 6 0.5 4.5 0.5 3.6 A3.5 3.5 0 0 1 7.5 3.6 C7.5 4.5 7 6 4 10Z" fill="none" stroke="#1fb3ea" stroke-width="1.2"/><circle cx="4" cy="3.6" r="1.1" fill="#1fb3ea"/></svg>
  </div>
  <p class="info-text" style="top:977px">Terranova Watch<br>14 Harbor Lane, Springfield</p>
  <div class="info-icon" style="top:1014px">
    <svg width="9" height="9" viewBox="0 0 10 10"><path d="M2 0.5 L4 3 L3 4.2 Q4.3 6 5.8 7 L7 6 L9.5 8 L8.2 9.5 Q4 9 0.5 1.8 Z" fill="#1fb3ea"/></svg>
  </div>
  <p class="info-text" style="top:1017px">1 800 555 0142</p>
  <div class="info-icon" style="top:1045px">
    <svg width="10" height="8" viewBox="0 0 10 8"><rect width="10" height="8" rx="1" fill="#1fb3ea"/><path d="M0.5 1 L5 4.5 L9.5 1" fill="none" stroke="#fff" stroke-width="1"/></svg>
  </div>
  <p class="info-text" style="top:1047px">hello@terranovawatch.in</p>

  <h3 class="col-title" style="left:478px;top:1078px">Newsletter Sign Up</h3>
  <div class="newsletter">
    <div class="email">Email Address</div>
    <div class="go">SIGN UP</div>
  </div>
</section>

<footer>
  <div class="footer-rule"></div>
  <p class="copyright">Copyright © 2017, Terranova Watch. All rights reserved.</p>
  <div class="social">
    <span style="background:#3b5998"></span>
    <span style="background:#1da1f2"></span>
    <span style="background:#1f87b8"></span>
    <span style="background:#cb2027"></span>
  </div>
</footer>

</body>
</html>
```